DELVOR Flyer

We would like the option of being able to fill in a text box so we would need an editable file to type in our information.
You can add wording to it yourself where you see fit
We would like better designs than the ones we are sending as well.
We would like the cedar vale logo add on the flyer. We want the exact logo but not the back ground. We would like the logo to show up multiple times if possible.
You are free to be creative with the design. If you have ideas that are not listed in the description, feel free to design them.
Thanks!!!
Family Insurance

```html
<!DOCTYPE html>
<html lang="en">
<head>
<meta charset="utf-8">
<title>DELVOR Flyer</title>
<link href="https://fonts.googleapis.com/css2?family=Lato:wght@400;700;900&family=Alegreya:ital@1&display=swap" rel="stylesheet">
<style>
  :root{
    --brand-red:#e0202b;
    --coral:#f25c62;
    --navy:#2d4f78;
    --slate-blue:#a3b3c8;
    --charcoal:#333338;
    --charcoal-dark:#26262a;
    --charcoal-mid:#4a4a50;
    --band-gray:#545459;
    --black:#050505;
    --white:#ffffff;
    --phone-text:#dfe6f0;
  }
  *{box-sizing:border-box;margin:0;padding:0}
  html,body{width:900px;height:1200px;overflow:hidden;background:var(--white)}
  body{font-family:"Lato",Arial,sans-serif;position:relative}
  .flyer{position:absolute;inset:0;width:900px;height:1200px;background:var(--white)}

  .brand{position:absolute;display:flex;align-items:center;gap:10px;color:var(--brand-red);font-weight:900;font-size:44px;letter-spacing:-1px;line-height:1}
  .brand-dot{width:34px;height:34px;border-radius:50%;background:var(--brand-red)}

  .header .brand{left:40px;top:40px}
  .header-accent{position:absolute;left:449px;top:0;width:53px;height:122px;background:var(--slate-blue)}
  .email-box{position:absolute;left:502px;top:0;width:398px;height:122px;background:var(--navy);padding:32px 0 0 26px}
  .email-label{color:var(--coral);font-weight:700;font-size:25px;letter-spacing:.5px}
  .email-value{color:var(--white);font-weight:700;font-size:20px;margin-top:4px}

  .top-band{position:absolute;left:0;top:122px;width:900px;height:22px;background:var(--band-gray)}

  .portrait-edge{position:absolute;left:0;top:144px;width:405px;height:15px;background:var(--coral)}
  .portrait{position:absolute;left:0;top:159px;width:405px;height:503px;
    background:linear-gradient(180deg,#6f7d4d 0%,#8e8a6a 30%,#b8b1a4 55%,#9c9890 80%,#7c7f72 100%)}

  .features{position:absolute;left:0;top:662px;width:405px;height:313px;background:var(--charcoal-mid);list-style:none;padding-top:44px}
  .features li{height:33.5px;display:flex;align-items:center;padding-left:24px;color:var(--white);font-weight:700;font-size:19px;border-top:3px solid var(--charcoal-mid)}
  .features li:nth-child(odd){background:var(--charcoal)}
  .features li:nth-child(even){background:var(--charcoal-dark)}
  .features li::before{content:"*";font-size:30px;margin-right:20px;line-height:1;padding-top:10px}

  .info-panel{position:absolute;left:405px;top:144px;width:495px;height:837px;background:var(--coral);padding:20px 22px 0 20px;overflow:hidden}
  .info-title{font-family:"Alegreya",Georgia,serif;font-style:italic;font-weight:400;font-size:29px;color:var(--white);margin-bottom:8px;letter-spacing:.3px;line-height:36px}
  .info-panel p{color:var(--white);font-weight:700;font-size:14px;line-height:16.5px;text-align:justify;hyphens:auto}
  .info-panel p + p{margin-top:16px}
  .info-panel p.tight{margin-top:0}
  .info-panel p.inset{padding:0 6px 0 8px}

  .bottom-band{position:absolute;left:0;top:981px;width:900px;height:44px;background:var(--black)}
  .bottom-line{position:absolute;left:0;top:1025px;width:900px;height:13px;background:var(--band-gray)}

  .phone-box{position:absolute;left:0;top:1066px;width:418px;height:134px;background:var(--navy);padding:26px 0 0 52px}
  .phone-label{color:var(--coral);font-weight:700;font-size:26px}
  .phone-value{color:var(--phone-text);font-weight:700;font-size:23px;margin-top:4px}
  .footer-accent{position:absolute;left:418px;top:1066px;width:57px;height:134px;background:var(--slate-blue)}
  .footer .brand{right:140px;top:1112px}
</style>
</head>
<body>
<main class="flyer">
  <header class="header">
    <div class="brand"><span class="brand-dot"></span>Cedar Vale</div>
    <div class="header-accent"></div>
    <div class="email-box">
      <div class="email-label">EMAIL:</div>
      <div class="email-value">Finibus Bonorum et Malorum"</div>
    </div>
  </header>

  <div class="top-band"></div>
  <div class="portrait-edge"></div>
  <div class="portrait" role="img" aria-label="Portrait photo of the insurance agent in a light suit, arms crossed, outdoors"></div>

  <ul class="features">
    <li>Lorem Ipsum is simply</li>
    <li>Lorem Ipsum is simply</li>
    <li>Lorem Ipsum is simply</li>
    <li>Lorem Ipsum is simply</li>
    <li>Lorem Ipsum is simply</li>
    <li>Lorem Ipsum is simply</li>
    <li>Lorem Ipsum is simply</li>
  </ul>

  <section class="info-panel">
    <h1 class="info-title">What is Lorem Ipsum?</h1>
    <p>Lorem Ipsum is simply dummy text of the printing and typesetting industry. Lorem Ipsum has been the industry's standard dummy text ever since the 1500s, when an unknown printer took a galley of type and scrambled it to make a type specimen book. It has survived not only five centuries, but also the leap into electronic typesetting, remaining essentially unchanged. It was popularised in the 1960s with the release of Pressmark sheets containing Lorem Ipsum passages, and more recently with desktop publishing software like Quillset Layout including versions of Lorem Ipsum.</p>
    <p class="tight">orem Ipsum is simply dummy text of the printing and typesetting industry. Lorem Ipsum has been the industry's standard dummy text ever since the 1500s, when an unknown printer took a galley of type and scrambled it to make a type specimen book. It has survived not only five centuries, but also the leap into electronic typesetting, remaining essentially unchanged. It was popularised in the 1960s with the release of Pressmark sheets containing Lorem Ipsum passages, and more recently with desktop publishing software like Quillset Layout including versions of Lorem Ipsum.</p>
    <p class="inset">orem Ipsum is simply dummy text of the printing and typesetting industry. Lorem Ipsum has been the industry's standard dummy text ever since the 1500s, when an unknown printer took a galley of type and scrambled it to make a type specimen book. It has survived not only five centuries, but also the leap into electronic typesetting, remaining essentially unchanged. It was popularised in the 1960s with the release of Leorem Ipsum is simply dummy text of the printing and typesetting industry. Lorem Ipsum has been the industry's standard dummy text ever since the 1500s, when an unknown printer took a galley of type and scrambled it to make a type specimen book. It has survived not only five centuries, but also the leap into electronic typesetting, remaining essentially unchanged. It was popularised in the</p>
    <p class="inset">orem Ipsum is simply dummy text of the printing and typesetting industry. Lorem Ipsum has been the industry's standard dummy text ever since the 1500s, when an unknown printer took a galley of type and scrambled it to make a type specimen book. It has survived not only five centuries, but also the leap into electronic typesetting, remaining essentially unchanged. It was popularised in the 1960s with the release of Leorem Ipsum is simply dummy text of the printing and typesetting industry. Lorem Ipsum has been the industry's standard dummy text ever since the 1500s, when an unknown printer took a galley of type and scrambled it to make a type specimen book. It has survived not only five centuries, but also the leap into electronic</p>
  </section>

  <div class="bottom-band"></div>
  <div class="bottom-line"></div>

  <footer class="footer">
    <div class="phone-box">
      <div class="phone-label">Phn no:</div>
      <div class="phone-value">1.10.32 and 1.10.33</div>
    </div>
    <div class="footer-accent"></div>
    <div class="brand"><span class="brand-dot"></span>Cedar Vale</div>
  </footer>
</main>
</body>
</html>
```